Tovimerra: Travel business card redesign

We need a clean elegant look for our cards featuring blue and orange. Look should communicate a sense of strong design and seem uncluttered. The company is Tovimerra which means escape to bliss. As in every trip is an escape to bliss. Feel free to reinvent the logo or just tweak it. Colors should be blue like Caribbean waters and a saturated orange. Keep it clean and simple.
Please match the information in the sample uploaded but the sample is horrible -- a non-starter -- use for information only. also please add managing director to my name as title

Target Market(s)
potential clients, hotels, trade publications
Industry/Entity Type
Travel Industry
Contact Information for Business Card
as above
Requirements
Must have
- Font should be century gothic. Colors below are close but a but prefer lighter in each case.

```html
<!DOCTYPE html>
<html lang="en">
<head>
<meta charset="utf-8">
<title>Tovimerra Business Cards</title>
<link rel="stylesheet" href="https://fonts.googleapis.com/css2?family=Questrial&display=swap">
<style>
  :root {
    --stage: #111112;
    --orange: #ea862b;
    --blue: #4aa3d6;
    --paper: #fbf8f3;
    --ink: #3a3a3a;
    --white: #ffffff;
  }
  * { margin: 0; padding: 0; box-sizing: border-box; }
  html, body {
    width: 1200px; height: 1000px; overflow: hidden;
    background: var(--stage);
    font-family: "Questrial", "Century Gothic", sans-serif;
  }
  .stage { position: relative; width: 1200px; height: 1000px; }
  .card {
    position: absolute; width: 520px; height: 297px;
    top: 352px; overflow: hidden;
  }
  .card--back { left: 50px; background: var(--orange); }
  .card--front { left: 630px; background: var(--paper); }

  .brand-name {
    position: absolute; font-size: 50px; letter-spacing: -1px; line-height: 1;
  }
  .card--back .brand-name {
    color: var(--white); left: 0; right: 0; top: 118px; text-align: center;
  }
  .card--front .brand-name { color: var(--orange); left: 150px; top: 38px; }

  .name-band {
    position: absolute; left: 0; top: 138px; width: 242px; height: 42px;
    background: var(--orange); color: var(--white);
    font-size: 20px; line-height: 42px; padding-left: 32px;
  }
  .accent-bar {
    position: absolute; left: 250px; top: 134px; width: 6px; height: 54px;
    background: var(--blue);
  }
  .job-title {
    position: absolute; left: 32px; top: 194px; font-size: 13px; color: var(--ink);
  }
  .contact-list {
    position: absolute; left: 282px; top: 140px; list-style: none;
    font-size: 14.5px; color: var(--ink); line-height: 19px;
  }
  .contact-list li { display: flex; align-items: flex-start; gap: 8px; }
  .contact-list svg { width: 12px; height: 14px; margin-top: 3px; flex: none; fill: var(--blue); }
</style>
</head>
<body>
<main class="stage">
  <section class="card card--back" aria-label="Card back">
    <div class="brand-name">Tovimerra</div>
  </section>

  <section class="card card--front" aria-label="Card front">
    <div class="brand-name">Tovimerra</div>
    <div class="name-band">Reed Halvorsen</div>
    <div class="accent-bar"></div>
    <div class="job-title">Managing Director</div>
    <ul class="contact-list">
      <li>
        <svg viewBox="0 0 12 14" aria-hidden="true"><path d="M2 1h3l1 3-2 1.5c.8 1.8 1.8 2.8 3.5 3.5L9 7l3 1v3c0 1-1 2-2 2C5 13 1 9 0 3c0-1 1-2 2-2z"/></svg>
        <span>877.55.TOVI (868400)</span>
      </li>
      <li>
        <svg viewBox="0 0 12 14" aria-hidden="true"><path d="M3 0h6a1 1 0 0 1 1 1v12a1 1 0 0 1-1 1H3a1 1 0 0 1-1-1V1a1 1 0 0 1 1-1zm.5 1.5v9h5v-9zM6 11.3a.9.9 0 1 0 0 1.8.9.9 0 0 0 0-1.8z"/></svg>
        <span>323.555.0142</span>
      </li>
      <li>
        <svg viewBox="0 0 12 14" aria-hidden="true"><path d="M3 1h6v3H3zM1 5h10a1 1 0 0 1 1 1v4H10v3H2v-3H0V6a1 1 0 0 1 1-1zm2 5v2h6v-2z"/></svg>
        <span>310.555.0187</span>
      </li>
      <li>
        <svg viewBox="0 0 12 14" aria-hidden="true"><path d="M6 0a5 5 0 0 1 5 5c0 3.5-5 9-5 9S1 8.5 1 5a5 5 0 0 1 5-5zm0 3a2 2 0 1 0 0 4 2 2 0 0 0 0-4z"/></svg>
        <span>1460 Harbor Crest Loop<br>N. Marlow Bay, 90817</span>
      </li>
    </ul>
  </section>
</main>
</body>
</html>
```